Business Card Design

I will be finding aged care homes for those who need placement.
Assisting with all of the paperwork.
I would like Australian wattle picture on the card/ logo please
Industry/Entity Type
Business
Contact Information for Business Card
Senior Living Pathways
Marla Jensen
PH: 0438 926 153
Email: seniorlivingpathways@mailbox.example
ABN: 63 214 958 307
PO Box 3189, Kallangur QLD 4503

```html
<!DOCTYPE html>
<html lang="en">
<head>
<meta charset="utf-8">
<title>Marla Jensen – Senior Living Pathways</title>
<link rel="stylesheet" href="https://fonts.googleapis.com/css2?family=Arvo&family=Open+Sans:wght@700&family=Questrial&display=swap">
<style>
  :root {
    --card-white: #ffffff;
    --ink: #0a0a0a;
    --leaf-green: #33e60f;
    --wattle-yellow: #f7ee00;
    --band-sage: #748f81;
    --band-edge: #e8f6dc;
    --band-text: #ffffff;
  }
  * { margin: 0; padding: 0; box-sizing: border-box; }
  html, body {
    width: 1200px;
    height: 741px;
    overflow: hidden;
    background: var(--card-white);
  }
  .card {
    position: relative;
    width: 1200px;
    height: 741px;
    background: var(--card-white);
    overflow: hidden;
  }
  .brand-mark {
    position: absolute;
    left: 55px;
    top: 115px;
    width: 328px;
    height: 328px;
  }
  .contact-block {
    position: absolute;
    right: 76px;
    top: 140px;
    text-align: right;
  }
  .holder-name {
    font-family: "Arvo", serif;
    font-size: 68px;
    line-height: 1;
    color: var(--ink);
  }
  .business-name {
    margin-top: 12px;
    font-family: "Questrial", sans-serif;
    font-size: 52px;
    line-height: 1;
    color: var(--leaf-green);
  }
  .phone, .email {
    font-family: "Open Sans", sans-serif;
    font-weight: 700;
    color: var(--leaf-green);
    line-height: 1;
  }
  .phone { margin-top: 30px; font-size: 37px; }
  .email { margin-top: 14px; font-size: 31px; }
  .footer-band {
    position: absolute;
    left: 0;
    right: 0;
    top: 515px;
    bottom: 0;
    border-top: 13px solid var(--band-edge);
    background: var(--band-sage);
  }
  .footer-details {
    position: absolute;
    left: 70px;
    top: 63px;
    font-family: "Arvo", serif;
    font-size: 35px;
    color: var(--band-text);
    white-space: nowrap;
  }
</style>
</head>
<body>
  <main class="card">
    <svg class="brand-mark" viewBox="0 0 328 328" aria-label="Senior Living Pathways">
      <circle cx="164" cy="164" r="158" fill="none" stroke="var(--wattle-yellow)" stroke-width="5"/>
      <text x="164" y="130" text-anchor="middle" font-family="Questrial, sans-serif" font-size="34" fill="var(--leaf-green)">Senior</text>
      <text x="164" y="174" text-anchor="middle" font-family="Questrial, sans-serif" font-size="34" fill="var(--leaf-green)">Living</text>
      <text x="164" y="218" text-anchor="middle" font-family="Questrial, sans-serif" font-size="34" fill="var(--leaf-green)">Pathways</text>
    </svg>

    <section class="contact-block">
      <h1 class="holder-name">Marla Jensen</h1>
      <p class="business-name">Senior Living Pathways</p>
      <p class="phone">PH: 0438 926 153</p>
      <p class="email">seniorlivingpathways@mailbox.example</p>
    </section>

    <footer class="footer-band">
      <p class="footer-details">ABN: 63 214 958 307 PO Box 3189, Kallangur QLD 4503</p>
    </footer>
  </main>
</body>
</html>
```